Book: The Seasoned Steward - Good Living IS NOT a Bystander Game

This book is about taking action, and being involved in making health decisions. The title of the book tells two things. First, this book helps people control their health outcomes better. Secondly, that you cannot get great results by just letting doctors make decisions for you (as a spectator). A cover could either show (1) An empowered patient who is "examining" or "influencing" their health outcomes, OR (2) A passive patient watching what is happening. It can be abstract.

All this is for the back of the book: You have been led to believe that two things count when it comes to outcomes: the skills of our practitioners and the effectiveness of the treatments they provide. You don’t even factor yourself into the equation! But you certainly should. You would not want a mediocre doctor, so why be a so-so patient or a passive healthcare consumer? The more evolved and involved you are as a patient and consumer, the closer your healthcare will come to match your needs and your goals. The archetypical relationship we have with healthcare providers needs to be kicked to the curb; it is not in your best interests. You are often being shortchanged, and I intend to let you know why. Reviews This book makes you reflect on your health further and helps you “invest in prevention". It makes you bolder and more conscious of how to navigate the healthcare system. All in all, The Seasoned Steward is an eye-opener. Miriam Oswick, Certified Nutritionist Practitioner It pays to be informed and proactive with our health. If your goal is to become a smarter healthcare consumer and be more actively involved in your personal wellness, then The Seasoned Steward is required reading. Offering practical tips, principles and guidelines, this book is an important, straightforward resource to navigating the path of self-advocacy. Lorena Pavitt, Wellness Coach Once again, Dr. Imogen uses her experience, knowledge and research to give us the tools to take charge of our health. This is a gift. Imogen is an incredible researcher and brings forward a very balanced approach in her writings. Dr. Wendy Pruitt DDS. MBA The seasoned steward is “expertly” written. Dr. Haverly poses some thought-provoking questions that encourage one to change how they approach their health and retain some of the ‘power’ they have in influencing their own health and outcomes. Eleni Roula Papadimas BSc. Clinical Biologist, Consultant of Oncology unit, Kyrtos Hospital, Athens, Greece. Very interesting read! The book is written for You. It is very personable and relatable. Tons of useful and innovative information. Dr. Nino Gvelesiani, DDS About the author Dr. Imogen Haverly is an accomplished naturopathic doctor, author, blogger and speaker. She previously authored Canada’s most comprehensive book on food labels to date, The Savvy Pantry Keeper: A Primer on Grocery Tags and Tales. Her personal healing journey and triumph with fibromyalgia inspired her to become a relentless advocate for taking health into our own hands. This book is a continuation of that passion. Dr. Imogen, as @TheLectureMedic, dedicates much of her time teaching others how to think about their health.

Target Market(s)

Healthcare consumers. Ordinary people.

Industry/Entity Type

Health And Wellness

Font styles to use
Sans Serif
Other font styles liked:
• Simple and elegant

Colors
89d0c7
34a6d7

Requirements
Must have
• This book will be published
1) E-book in JPEG, PNG, TIFF
2) Printed book cover: 5.25"x8" (13.335x20.32 cm) (38,792 words)... pages about 160??? - provide in word file as well so I can edit
Image must be 2400X1600 pixels
3) Display of 3D book for advertisements
Nice to have
• *copy the design layout for my last book (BACK COVER) - attached
*attaching an example of an image from istock that is an EXAMPLE of a creative way to showing a patient being a SPECTATOR. I made a cover using it: https://www.pictovault-example.com/fr/vectoriel/calme-du-corps-gm908172635-71029384
*Nice elegant font (like in my example attached)
Should not have
• *avoid clipart of doctors or doctors with patients... this is too general

```html
<!DOCTYPE html>
<html lang="en">
<head>
<meta charset="utf-8">
<title>The Seasoned Steward — Book Cover</title>
<link rel="stylesheet" href="https://fonts.googleapis.com/css2?family=Montserrat:wght@400;700;800&display=swap">
<style>
  :root {
    --cover-blue-deep: #1a3fae;
    --cover-blue: #2350c4;
    --cover-blue-light: #2d61d6;
    --accent-teal: #89d0c7;
    --accent-sky: #34a6d7;
    --accent-lavender: #9fb3e0;
    --ink-white: #ffffff;
  }
  * { margin: 0; padding: 0; box-sizing: border-box; }
  html, body {
    width: 750px;
    height: 1200px;
    overflow: hidden;
    background: var(--cover-blue-deep);
  }
  .cover {
    position: relative;
    width: 750px;
    height: 1200px;
    overflow: hidden;
    background: radial-gradient(ellipse at 55% 35%, var(--cover-blue-light) 0%, var(--cover-blue) 50%, var(--cover-blue-deep) 100%);
    font-family: "Montserrat", Arial, sans-serif;
    color: var(--ink-white);
  }
  .corner-block {
    position: absolute;
    left: 37px;
    width: 93px;
    background: var(--accent-teal);
  }
  .corner-block--top { top: 0; height: 52px; }
  .corner-block--lower { top: 67px; height: 93px; }
  .author-name {
    position: absolute;
    top: 30px;
    left: 0;
    width: 100%;
    text-align: center;
    font-weight: 700;
    font-size: 17px;
    letter-spacing: 1px;
    text-transform: uppercase;
  }
  .book-title {
    position: absolute;
    top: 190px;
    left: 40px;
    font-weight: 800;
    font-size: 62px;
    line-height: 84px;
    text-transform: uppercase;
  }
  .title-rule {
    position: absolute;
    top: 470px;
    left: 45px;
    width: 312px;
    height: 3px;
    background: var(--ink-white);
  }
  .book-subtitle {
    position: absolute;
    top: 492px;
    left: 45px;
    font-weight: 400;
    font-size: 26px;
    line-height: 40px;
  }
  .book-subtitle strong { font-weight: 800; }
  .cover-artwork {
    position: absolute;
    left: 0;
    top: 0;
  }
</style>
</head>
<body>
  <main class="cover">
    <div class="corner-block corner-block--top"></div>
    <div class="corner-block corner-block--lower"></div>

    <p class="author-name">Dr. Imogen Haverly</p>

    <h1 class="book-title">The<br>Seasoned<br>Steward</h1>
    <div class="title-rule"></div>
    <p class="book-subtitle">Good Living <strong>IS NOT</strong><br>a Bystander Game</p>

    <svg class="cover-artwork" width="750" height="1200" viewBox="0 0 750 1200"
         role="img" aria-label="Illustration of a white stethoscope whose tubing winds down into a looping segmented path in teal, sky blue and lavender, like a game board trail">
      <defs>
        <linearGradient id="artwork-tone" x1="0" y1="0" x2="0.3" y2="1">
          <stop offset="0" stop-color="#ffffff" stop-opacity="0.5"/>
          <stop offset="0.55" stop-color="#9fb3e0" stop-opacity="0.45"/>
          <stop offset="1" stop-color="#89d0c7" stop-opacity="0.55"/>
        </linearGradient>
      </defs>
      <rect x="400" y="150" width="275" height="640" rx="120" fill="url(#artwork-tone)"/>
      <rect x="112" y="620" width="660" height="520" rx="230" fill="url(#artwork-tone)"/>
    </svg>
  </main>
</body>
</html>
```